We are a full service general contractor that specializes in emergency services and insurance restoration/repair. Most of our work relates to water damage, fire dame, smoke, wind and hail, storm damage, etc. Pretty much anything you would call your insurance company for.

On one side of card the logo is VERY easy with the possibility of some modifications once I get a preview. I had a logo designed years ago and its on all my vehicles so I want to stick with my branding at this point and time.

Its a 2 sided card-for one side I would like the following:
* See logo (its attached)
* I would like this logo as large/big/bold as possible-essentially it should fill up the entire side of the card (barring it not looking proportionally correct of course)
* I think the background should be white behind it-or possibly red (with colors inverted so that they don't get lost in the red background)
* I'm attaching a photo of one of our work vans to go off of-you will notice that the .com wraps up the side of the logo-this .com portion needs to added on as the logo is only the crest renewal logo

The other side of the card I'm thinking should be:
* My biggest struggle is formatting-in other words-I don't know how to lay out all that info without the card looking jumbled/messy
* all our logos, vehicles, marketing media, etc. is based on or at least inspired by a clean look
* a smaller version of logo (without the .com) should be located somewhere on this side of card-I've seen some cards where its centered and others where its offset-I'm not sure which is better
* I could conceivably leave off PO BOX if its too much info and something needs deleted

The logo will display company name-other pertinent info:
Phone: 704 555 0183
Mobile: 704 555 0147
Fax: 704 555 0192
email: crestrenewal@mailhub.example
Address: 2583 Elm Rd.
Charlotte, NC
PO BOX 36502 28299

```html
<!DOCTYPE html>
<html lang="en">
<head>
<meta charset="utf-8">
<title>Crest Renewal — Business Card</title>
<link rel="stylesheet" href="https://fonts.googleapis.com/css2?family=Source+Sans+3:wght@400;800&display=swap">
<style>
  :root {
    --stage: #3a3431;
    --card: #0d0d0d;
    --ink-light: #f2f2f2;
    --silver: #c9c9c9;
    --brand-red: #d8262c;
    --divider: #7a1a1d;
  }
  * { box-sizing: border-box; margin: 0; padding: 0; }
  html, body {
    width: 1200px;
    height: 900px;
    overflow: hidden;
    background: var(--stage);
    font-family: "Source Sans 3", "Myriad Pro", sans-serif;
  }
  .stage {
    position: relative;
    width: 1200px;
    height: 900px;
  }
  .card {
    position: absolute;
    top: 304px;
    width: 510px;
    height: 292px;
    background: var(--card);
    box-shadow: 0 10px 28px rgba(0,0,0,.45);
  }
  .card--back { left: 60px; }
  .card--front { left: 630px; display: flex; align-items: center; justify-content: center; }

  /* brand name lockup */
  .brand {
    display: flex;
    align-items: center;
    gap: 10px;
    font-weight: 800;
    text-transform: uppercase;
    line-height: 1;
    letter-spacing: .01em;
  }
  .brand__square { flex: none; }
  .brand--front { color: var(--silver); font-size: 44px; gap: 14px; }
  .brand--front .brand__square { width: 34px; height: 34px; background: var(--silver); }
  .brand--back {
    position: absolute;
    left: 26px;
    top: 150px;
    color: var(--brand-red);
    font-size: 22px;
  }
  .brand--back .brand__square { width: 18px; height: 18px; background: var(--brand-red); }

  .divider {
    position: absolute;
    left: 258px;
    top: 40px;
    width: 1px;
    height: 210px;
    background: var(--divider);
  }
  .contact {
    position: absolute;
    left: 272px;
    top: 42px;
    color: var(--ink-light);
    font-size: 14.5px;
    line-height: 1.3;
    font-weight: 400;
  }
  .contact__address { margin-bottom: 8px; }
  .contact__list { list-style: none; }
  .contact__item { display: flex; align-items: center; gap: 9px; }
  .contact__icon { width: 10px; height: 10px; flex: none; fill: var(--brand-red); }
</style>
</head>
<body>
<main class="stage">

  <section class="card card--back" aria-label="Card back with contact details">
    <div class="brand brand--back">
      <span class="brand__square"></span>
      <span class="brand__name">crest renewal</span>
    </div>
    <div class="divider"></div>
    <div class="contact">
      <p class="contact__address">2583 Elm Rd.<br>Charlotte, NC<br>PO BOX 36502 28299</p>
      <ul class="contact__list">
        <li class="contact__item">
          <svg class="contact__icon" viewBox="0 0 10 10" aria-hidden="true"><path d="M2 0.5 L3.6 2.6 L2.7 3.6 Q4 6 6.4 7.3 L7.4 6.4 L9.5 8 L8.3 9.5 Q3.5 9 0.5 1.7 Z"/></svg>
          <span>704 555 0183</span>
        </li>
        <li class="contact__item">
          <svg class="contact__icon" viewBox="0 0 10 10" aria-hidden="true"><path d="M2.5 0 H7.5 V10 H2.5 Z M3.4 1.2 V8 H6.6 V1.2 Z"/></svg>
          <span>704 555 0147</span>
        </li>
        <li class="contact__item">
          <svg class="contact__icon" viewBox="0 0 10 10" aria-hidden="true"><path d="M2.5 0 H7 V3 H9.5 V10 H0.5 V3 H2.5 Z M3.4 0.9 V3 H6.1 V0.9 Z M2 5 V6 H8 V5 Z M2 7 V8 H8 V7 Z"/></svg>
          <span>704 555 0192</span>
        </li>
        <li class="contact__item">
          <svg class="contact__icon" viewBox="0 0 10 10" aria-hidden="true"><path d="M0 2 H10 V8.5 H0 Z M0.9 2.8 L5 5.8 L9.1 2.8 Z"/></svg>
          <span>crestrenewal@mailhub.example</span>
        </li>
      </ul>
    </div>
  </section>

  <section class="card card--front" aria-label="Card front with company name">
    <div class="brand brand--front">
      <span class="brand__square"></span>
      <span class="brand__name">crest renewal</span>
    </div>
  </section>

</main>
</body>
</html>
```